Holiday Let Property Management Service and Website. We manage properties for holiday letting

We want a stylish business card that reflects our brand.
*** UPDATE *** PLEASE USE THE RECTANGULAR ORANGE COLOUR SWIPE PROVIDED IN THE DROP BOX FOR THE BSINESS CARD COLOUR.***
Please view the site: www.lodgewell.com.au
Obviously, we want to use the same logo font from our site for the card design.
We want to have the name "Staywisely" right across the front in white and an orange background colour that matches the orange on our website or a brighter fresher looking orange .
We'd like to have the details on the back similar to what I've shown below but obviously with some more aesthetic added and better positioning than I have provided.
Same colours as the front. white writing and orange background. Once we have the design we'd like the font to be raised and the finish to be a low sheen. Quality thickness and finishes.
---------------------------------------------------------------------------
(Rough idea of writing details on back of card but open to nicer repositioning)

STAYWISELY
Holiday Let Management & Consulting Specialists

Marta Okonkwo Glen Farrow
Principal Director
0427360958 0438671254

email: enquiries@lodgewell.com.au
www.lodgewell.com.au

--------------------------------------------------------------------------

Target Market(s)

Property owners who may want to convert to holiday letting and people seeking holiday accommodation.

Industry/Entity Type

Tourism

Contact Information for Business Card

(Front of card) To have "Staywisely" to stretch across the card in white writing the same font as our website home page. (discreetly including the logo TM if possible)

------------------------------------------------------------------------------------------------
(Back of card)

STAYWISELY
Holiday Let Consultants & Management Specialists

Marta Okonkwo Glen Farrow
Principal Director
0427360958 0438671254

www.lodgewell.com.au

-----------------------------------------------------------------------------------------------

Font styles to use
Other font styles liked:
• something similar or complimentary to our logo font please

Requirements
Must have
• The same font for our logo name and close to the same colour orange as the orange footer on our website. (if you can make it pop more without going too far away from it that would be great.)
• Orange background front and back with white font.
• *** UPDATE *** PLEASE USE THE RECTANGULAR ORANGE COLOUR SWIPE PROVIDED IN THE DROP BOX FOR THE BSINESS CARD COLOUR.***
Nice to have
• Great symmetry and aesthetics
Should not have
• Any other writing except our brand name (Staywisely) on the front of the card and a small, discreet trade mark (TM)

```html
<!DOCTYPE html>
<html lang="en">
<head>
<meta charset="utf-8">
<title>Staywisely Business Card</title>
<link href="https://fonts.googleapis.com/css2?family=Roboto:wght@400;500;700&display=swap" rel="stylesheet">
<style>
  :root {
    --orange: #e8933c;
    --white: #ffffff;
    --ink: #231f20;
    --rule: #5a5a5a;
  }
  * { margin: 0; padding: 0; box-sizing: border-box; }
  html, body { width: 1200px; height: 1200px; overflow: hidden; background: var(--white); }
  body { position: relative; font-family: "Roboto", Arial, sans-serif; }

  .card { position: absolute; left: 180px; width: 838px; height: 478px; border-radius: 38px; overflow: hidden; }

  .card-front { top: 100px; background: var(--orange); color: var(--white); }
  .front-wordmark {
    position: absolute; left: 0; right: 0; top: 246px;
    text-align: center; font-weight: 700; font-size: 108px; line-height: 1;
    letter-spacing: -4px;
  }
  .front-wordmark .tm { position: absolute; font-size: 12px; letter-spacing: 0; margin-left: 6px; margin-top: 6px; }
  .front-tagline {
    position: absolute; left: 0; right: 0; top: 374px;
    text-align: center; font-weight: 700; font-size: 26px; letter-spacing: 0.8px;
  }

  .card-back { top: 619px; background: var(--white); border: 1px solid var(--rule); }
  .brand-block { position: absolute; left: 75px; top: 137px; width: 181px; }
  .brand-square { width: 181px; height: 181px; background: var(--orange); }
  .brand-name { margin-top: 4px; color: var(--orange); font-weight: 500; font-size: 25px; letter-spacing: -1px; text-align: center; line-height: 1; }

  .person { position: absolute; left: 284px; top: 136px; color: var(--ink); }
  .person-name { font-weight: 700; font-size: 30px; letter-spacing: 0.3px; line-height: 1.1; }
  .person-role { font-weight: 400; font-size: 22px; margin-top: 4px; }

  .contacts { position: absolute; left: 284px; top: 233px; list-style: none; color: var(--ink); font-size: 25px; }
  .contacts li { display: flex; align-items: center; height: 37px; }
  .contacts svg { width: 22px; height: 22px; margin-right: 20px; flex: none; }

  .side-band { position: absolute; right: 0; top: 137px; width: 50px; height: 204px; background: var(--orange); }
</style>
</head>
<body>
  <section class="card card-front">
    <div class="front-wordmark">Staywisely<span class="tm">TM</span></div>
    <div class="front-tagline">Holiday Let Management &amp; Consulting Specialists</div>
  </section>

  <section class="card card-back">
    <div class="brand-block">
      <div class="brand-square"></div>
      <div class="brand-name">Staywisely</div>
    </div>

    <div class="person">
      <div class="person-name">Marta Okonkwo Glen Farrow</div>
      <div class="person-role">Principal Director</div>
    </div>

    <ul class="contacts">
      <li>
        <svg viewBox="0 0 22 22" aria-hidden="true"><rect x="5" y="1.5" width="12" height="19" rx="3" fill="none" stroke="#e8933c" stroke-width="2"/><circle cx="11" cy="17" r="1.4" fill="#e8933c"/></svg>
        0427360958 0438671254
      </li>
      <li>
        <svg viewBox="0 0 22 22" aria-hidden="true"><rect x="1" y="5" width="20" height="13" fill="#e8933c"/><path d="M1 5 L11 12 L21 5 M1 18 L8.5 10.5 M21 18 L13.5 10.5" fill="none" stroke="#fff" stroke-width="1.4"/></svg>
        enquiries@lodgewell.com.au
      </li>
      <li>
        <svg viewBox="0 0 22 22" aria-hidden="true"><g fill="none" stroke="#e8933c" stroke-width="1.8"><circle cx="11" cy="11" r="9"/><ellipse cx="11" cy="11" rx="4" ry="9"/><path d="M2 11 H20 M3.5 6.5 H18.5 M3.5 15.5 H18.5"/></g></svg>
        www.lodgewell.com.au
      </li>
    </ul>

    <div class="side-band"></div>
  </section>
</body>
</html>
```